Three Self-help Book Covers for BRG

We need three book covers designed.

We have a good idea what the three designs will be and our directions are attached along with sample artwork.

1-Nine Quiet Lanterns
2-The PaperKite Almanac
3-The Driftwood

My schools website is: www.BrightmoorRiverGuild.example

Target Market(s)

Self-help

Industry/Entity Type

Life Coaching

Font styles to use
Other font styles liked:
• See Attachment for details

Requirements
Must have
• See Attached Suggestions
Nice to have
Should not have

```html
<!DOCTYPE html>
<html lang="en">
<head>
<meta charset="utf-8">
<title>The PaperKite Almanac – Cover Wrap</title>
<link rel="stylesheet" href="https://fonts.googleapis.com/css2?family=Fredoka:wght@600&family=Kalam:wght@700&family=Arimo:wght@400;700&display=swap">
<style>
  :root {
    --parchment-light: #d6c998;
    --parchment-mid: #c3b27b;
    --parchment-dark: #8f7c48;
    --title-olive: #6e7d22;
    --title-olive-deep: #4b5612;
    --ink-dark: #2e2a17;
    --ink-brown: #3a2e1a;
    --gold-light: #f3d77a;
    --gold-mid: #c99a2e;
    --gold-dark: #8a6413;
    --string-blue: #5b6f9a;
    --photo-sky: #a9d3e6;
    --photo-skin: #e9c2a6;
  }
  html, body {
    margin: 0;
    padding: 0;
    width: 1200px;
    height: 850px;
    overflow: hidden;
    background: var(--parchment-mid);
  }
  .cover-wrap {
    position: relative;
    width: 1200px;
    height: 850px;
    overflow: hidden;
    background:
      radial-gradient(ellipse at 45% 40%, var(--parchment-light) 0%, var(--parchment-mid) 55%, var(--parchment-dark) 100%);
  }
  .hanging-art {
    position: absolute;
    left: 0;
    top: 0;
    width: 1200px;
    height: 850px;
  }
  .title-block {
    position: absolute;
    left: 724px;
    width: 400px;
    top: 28px;
    text-align: center;
  }
  .book-title {
    margin: 0;
    font-family: "Fredoka", "Arial Rounded MT Bold", sans-serif;
    font-weight: 600;
    color: var(--title-olive);
    line-height: 0.9;
    text-shadow: 0 3px 0 var(--title-olive-deep), 0 6px 8px rgba(40, 30, 10, 0.45);
  }
  .book-title .title-the {
    display: block;
    font-size: 54px;
  }
  .book-title .title-main {
    display: block;
    font-size: 66px;
  }
  .book-title .title-second {
    display: block;
    font-size: 76px;
  }
  .book-subtitle {
    margin: 14px 0 0;
    font-family: "Kalam", "Comic Sans MS", cursive;
    font-weight: 700;
    font-size: 19px;
    color: var(--ink-dark);
  }
  .method-note {
    position: absolute;
    left: 624px;
    width: 600px;
    top: 708px;
    margin: 0;
    text-align: center;
    font-family: "Arimo", Arial, sans-serif;
    font-size: 15px;
    line-height: 1.5;
    color: var(--ink-dark);
  }
  .author-line {
    position: absolute;
    left: 624px;
    width: 600px;
    top: 797px;
    margin: 0;
    text-align: center;
    font-family: "Arimo", Arial, sans-serif;
    font-weight: 700;
    font-size: 15px;
    color: var(--ink-brown);
  }
</style>
</head>
<body>
<main class="cover-wrap">
  <svg class="hanging-art" viewBox="0 0 1200 850" xmlns="http://www.w3.org/2000/svg">
    <defs>
      <linearGradient id="gold-frame" x1="0" y1="0" x2="1" y2="1">
        <stop offset="0" stop-color="var(--gold-light)"/>
        <stop offset="0.45" stop-color="var(--gold-mid)"/>
        <stop offset="0.7" stop-color="var(--gold-light)"/>
        <stop offset="1" stop-color="var(--gold-dark)"/>
      </linearGradient>
      <linearGradient id="photo-tones" x1="0" y1="0" x2="0" y2="1">
        <stop offset="0" stop-color="var(--photo-sky)"/>
        <stop offset="0.45" stop-color="var(--photo-skin)"/>
        <stop offset="1" stop-color="#b58a62"/>
      </linearGradient>
      <radialGradient id="drop-shadow" cx="0.5" cy="0.5" r="0.5">
        <stop offset="0" stop-color="rgba(40,30,10,0.45)"/>
        <stop offset="1" stop-color="rgba(40,30,10,0)"/>
      </radialGradient>
    </defs>

    <g class="hanging-strings" stroke="var(--string-blue)" stroke-width="2.5" fill="none">
      <line x1="743" y1="0" x2="743" y2="262"/>
      <line x1="1104" y1="0" x2="1104" y2="262"/>
      <circle cx="743" cy="266" r="5"/>
      <circle cx="1104" cy="266" r="5"/>
    </g>

    <ellipse class="frame-shadow" cx="924" cy="640" rx="200" ry="26" fill="url(#drop-shadow)"/>

    <rect class="cover-photo" x="722" y="296" width="404" height="262" fill="url(#photo-tones)"
          role="img" aria-label="Photo of cupped hands holding wooden tags reading love, creation, self image, beliefs, transform, ego and dis-creation"/>

    <rect class="gold-frame" x="709" y="283" width="430" height="288" rx="4"
          fill="none" stroke="url(#gold-frame)" stroke-width="26"/>
    <rect class="gold-frame-inner-edge" x="722" y="296" width="404" height="262"
          fill="none" stroke="var(--gold-dark)" stroke-width="2"/>
  </svg>

  <header class="title-block">
    <h1 class="book-title">
      <span class="title-the">The</span>
      <span class="title-main">PaperKite</span>
      <span class="title-second">Almanac</span>
    </h1>
    <p class="book-subtitle">A Guide Book for the Inner You</p>
  </header>

  <p class="method-note">Based on the Life Coaching Training Method<br>that’s Changing the world “one soul at a time” The KiteMethod ™</p>

  <p class="author-line">by Master Coach Ren Halvorsen</p>
</main>
</body>
</html>
```